Design a menu for health restaurant

A health food restaurant in Los Angeles is seeking menu design. Our foods are made from scratch using whole ingredients.
Name: Grubb Larder
Address: 1000 E 60th StLos Angeles, CA 90247
Website: www.GrubbLarder.example
We are looking for a clean and simple menu. Brand colors are white/tan, green and orange.

Please see attached excel with menu items and logo. We do not yet have prices.

Colors
f78f20
9bcb3c
ffffff
fff3d1

Requirements
Must have
• Easy to read.
Trifold menu design (front and back).
VEGAN, VEGETARIAN, GLUTEN FREE, CONTAINS NUTS symbols.
Logo.
Nice to have
• Incorporate brand colors, but still be easy to read.
We would like to use the Belco font (attached) if it works. If not we are open to a similar font that is easy to read.

Please see attached images.
We like the images and headers of OPTION 1. Would like something similar in trifold format.
We like the clean fonts of OPTION 2.

```html
<!DOCTYPE html>
<html lang="en">
<head>
<meta charset="utf-8">
<title>Grubb Larder — Trifold Menu</title>
<link href="https://fonts.googleapis.com/css2?family=Questrial&family=Arimo:wght@400&display=swap" rel="stylesheet">
<style>
:root{
  --orange:#f78f20;
  --green:#9bcb3c;
  --cream:#fff3d1;
  --white:#ffffff;
  --ink:#3b3b3b;
  --muted:#6a6a6a;
  --wheat:#f2b705;
  --nut:#6b4424;
  --stage:#f1f1ef;
}
*{box-sizing:border-box;margin:0;padding:0}
html,body{width:1200px;height:537px;overflow:hidden;background:var(--stage)}
body{position:relative;font-family:"Arimo",Arial,sans-serif;color:var(--ink)}
.sheet{position:absolute;top:45px;width:585px;height:446px;background:var(--white);overflow:hidden;box-shadow:0 6px 18px rgba(0,0,0,.12)}
.sheet--outside{left:10px}
.sheet--inside{left:605px}
.block{position:absolute;padding:7px 8px 0 11px;overflow:hidden}
.bg-white{background:var(--white)}
.bg-cream{background:var(--cream)}
.bg-green{background:var(--green)}
.bg-orange{background:var(--orange)}
.photo{position:absolute}
.section-title{font-family:"Questrial",sans-serif;font-size:13.5px;color:var(--orange);letter-spacing:.2px;line-height:1;margin-bottom:3px;text-transform:uppercase}
.bg-green .section-title,.bg-orange .section-title{color:var(--white)}
.item{margin-bottom:4px}
.item-name{font-family:"Questrial",sans-serif;font-size:7.2px;color:var(--green);letter-spacing:.3px;line-height:1.15;display:flex;align-items:center;gap:2px;flex-wrap:wrap}
.bg-white .item-name{color:var(--orange)}
.bg-cream .item-name{color:var(--green)}
.bg-green .item-name,.bg-orange .item-name{color:var(--white)}
.price{font-size:5.6px;opacity:.85;margin-right:2px}
.item-desc{font-size:5.1px;line-height:1.22;color:var(--ink)}
.bg-green .item-desc,.bg-orange .item-desc{color:#fffbe9}
.ic{width:6px;height:6px;flex:none}
.legend{position:absolute;padding:5px 6px;display:flex;flex-direction:column;gap:4px}
.legend-row{display:flex;align-items:center;gap:6px;font-size:4.9px;color:var(--ink)}
.legend-row .ic{width:7px;height:7px}
.right{text-align:right}
.right .item-name{justify-content:flex-end}
.brand{position:absolute;display:flex;align-items:center;justify-content:center;gap:7px}
.brand-dot{width:22px;height:22px;border-radius:50%;background:var(--orange)}
.brand-name{font-family:"Questrial",sans-serif;font-size:19px;color:var(--orange);letter-spacing:.5px}
.closing{position:absolute;text-align:center;color:var(--white);font-family:"Questrial",sans-serif}
.closing-note{font-size:6.6px;line-height:1.35;letter-spacing:.3px;margin-bottom:8px}
.closing-contact{font-size:5.1px;line-height:1.5}
.note{font-style:italic;color:var(--ink);font-size:5px}
</style>
</head>
<body>
<svg width="0" height="0" style="position:absolute" aria-hidden="true">
  <symbol id="i-vegan" viewBox="0 0 10 10"><path d="M2 9C1 5 3 1 9 1c0 6-3 8-7 8z" fill="#7cb82f"/></symbol>
  <symbol id="i-veg" viewBox="0 0 10 10"><path d="M2 9C1 5 3 1 9 1c0 6-3 8-7 8z" fill="#f78f20"/></symbol>
  <symbol id="i-gf" viewBox="0 0 10 10"><path d="M5 10V4M5 5L2 2M5 5L8 2M5 7L2.5 4.5M5 7L7.5 4.5" stroke="#f2b705" stroke-width="1.4" fill="none" stroke-linecap="round"/></symbol>
  <symbol id="i-nut" viewBox="0 0 10 10"><ellipse cx="5" cy="5.5" rx="3.2" ry="4.2" fill="#6b4424"/></symbol>
</svg>

<!-- Outside of the trifold -->
<section class="sheet sheet--outside">
  <div class="block bg-white" style="left:0;top:0;width:196px;height:202px">
    <h2 class="section-title">Burgers n' Sammies</h2>
    <div class="item"><div class="item-name">Air Fried Chicken Sammy <span class="price">| 12.34</span></div><p class="item-desc">Air fried chicken breast topped with red leaf lettuce, tomato, house made pickles and Larder Sauce on a bun served with choice of salad or fries.</p></div>
    <div class="item"><div class="item-name">Grilled Chicken Sammy <span class="price">| 12.34</span></div><p class="item-desc">Grilled chicken topped with guacamole, red leaf lettuce, tomato, house made pickles and Larder Sauce. Served with regular fries or side salad.</p></div>
    <div class="item"><div class="item-name">Classic Beef Burger <span class="price">| 12.34</span></div><p class="item-desc">House seasoned beef burger topped with red leaf lettuce, tomato, cheddar cheese, house made pickles and Larder Sauce on a bun served with choice of salad or fries.</p></div>
    <div class="item"><div class="item-name">Black Bean Pine Nut Burger <span class="price">| 12.34</span><svg class="ic"><use href="#i-vegan"/></svg><svg class="ic"><use href="#i-nut"/></svg></div><p class="item-desc">House made black bean pine nut burger topped with red leaf lettuce, tomato, house made pickles and mustard aioli on a bun served with choice of salad or fries.</p></div>
    <div class="item"><div class="item-name">Salmon Burger <span class="price">| 12.34</span></div><p class="item-desc">House made salmon burger topped with red leaf lettuce, tomato, house made pickles and Larder yogurt on a bun served with choice of salad or fries.</p></div>
  </div>

  <div class="block bg-cream" style="left:0;top:202px;width:129px;height:129px">
    <h2 class="section-title">Snacks n' Sides</h2>
    <div class="item"><div class="item-name">Fries <span class="price">| 12.34</span><svg class="ic"><use href="#i-vegan"/></svg><svg class="ic"><use href="#i-gf"/></svg></div><p class="item-desc">Hand cut air-fries with house seasonings. Choose regular or sweet potato fries.</p></div>
    <div class="item"><div class="item-name">Side Salad <span class="price">| 12.34</span></div><p class="item-desc">Your choice of House, Golden Beet, Mediterranean, or Vegan Chef side salad. (24oz)</p></div>
    <div class="item"><div class="item-name">Guac + Chips <span class="price">| 12.34</span><svg class="ic"><use href="#i-vegan"/></svg><svg class="ic"><use href="#i-gf"/></svg></div><p class="item-desc">Guacamole with blue corn tortilla chips.</p></div>
    <div class="item"><div class="item-name">Hummus + Chips <span class="price">| 12.34</span><svg class="ic"><use href="#i-vegan"/></svg><svg class="ic"><use href="#i-gf"/></svg></div><p class="item-desc">Hummus with blue corn tortilla chips.</p></div>
  </div>
  <div class="photo" role="img" aria-label="Guacamole with a blue corn tortilla chip" style="left:129px;top:202px;width:67px;height:129px;background:linear-gradient(160deg,#8a8378,#b7b07a 55%,#d9d3a8)"></div>

  <div class="photo" role="img" aria-label="Mixed salad with hummus and vegetables" style="left:0;top:331px;width:78px;height:115px;background:linear-gradient(150deg,#5d7a34,#c9b66a 50%,#6f8e3c)"></div>
  <div class="block bg-green right" style="left:78px;top:331px;width:118px;height:115px;padding:8px 10px 0 6px">
    <h2 class="section-title">Combos</h2>
    <div class="item"><div class="item-name">Soup + Salad <span class="price">| 12.34</span></div><p class="item-desc">Your choice of soup and side salad. 16oz soup + 38oz salad</p></div>
    <div class="item"><div class="item-name">Avo Toast Combo <span class="price">| 12.34</span></div><p class="item-desc">Half avocado toast and your choice of soup. 16oz</p></div>
    <div class="item"><div class="item-name">Soup + Sammy <span class="price">| 12.34</span></div><p class="item-desc">Your choice of soup and sandwich. 16oz soup + Sandwich</p></div>
  </div>

  <div class="block bg-cream" style="left:196px;top:0;width:195px;height:131px">
    <h2 class="section-title">Desserts</h2>
    <div style="width:112px">
    <div class="item"><div class="item-name">Date Coffee Cake <span class="price">| 12.34</span><svg class="ic"><use href="#i-vegan"/></svg><svg class="ic"><use href="#i-nut"/></svg></div><p class="item-desc">Signature date coffee cake with walnuts.</p></div>
    </div>
    <div class="item"><div class="item-name">Fruit + Spices <span class="price">| 12.34</span><svg class="ic"><use href="#i-vegan"/></svg><svg class="ic"><use href="#i-gf"/></svg></div><p class="item-desc">Strawberry, pineapple, green apple, orange, and blueberries with lime and chili seasoning.</p></div>
    <div class="item"><div class="item-name">Cookies <span class="price">| 12.34</span><svg class="ic"><use href="#i-veg"/></svg></div><p class="item-desc">Your choice of Chocolate Chip or Double Chocolate Chip fresh baked cookie.</p></div>
    <div class="item"><div class="item-name">Larder Chocolate Mousse <span class="price">| 12.34</span><svg class="ic"><use href="#i-vegan"/></svg><svg class="ic"><use href="#i-gf"/></svg></div><p class="item-desc">Served with grated dark chocolate.</p></div>
  </div>
  <div class="legend bg-white" style="left:316px;top:4px;width:73px;height:58px">
    <div class="legend-row"><svg class="ic"><use href="#i-vegan"/></svg>Vegan</div>
    <div class="legend-row"><svg class="ic"><use href="#i-veg"/></svg>Vegetarian</div>
    <div class="legend-row"><svg class="ic"><use href="#i-gf"/></svg>Gluten Free</div>
    <div class="legend-row"><svg class="ic"><use href="#i-nut"/></svg>Contains Nuts</div>
  </div>

  <div class="block bg-orange" style="left:196px;top:131px;width:195px;height:200px">
    <h2 class="section-title">Drinks</h2>
    <div class="item"><div class="item-name">Coffee <span class="price">| 12.34</span></div><p class="item-desc">We proudly serve Halden Coffee, a local roaster.</p></div>
    <div class="item"><div class="item-name">Power Date Shake <span class="price">| 12.34</span><svg class="ic"><use href="#i-vegan"/></svg><svg class="ic"><use href="#i-gf"/></svg></div><p class="item-desc">Ice-blended energy smoothie featuring dates and coffee.</p></div>
    <div class="item"><div class="item-name">Heart Beet Juice <span class="price">| 12.34</span><svg class="ic"><use href="#i-vegan"/></svg><svg class="ic"><use href="#i-gf"/></svg></div><p class="item-desc">Red beet, apple, carrot, ginger, parsley, and lemon.</p></div>
    <div class="item"><div class="item-name">Green Leafy Juice <span class="price">| 12.34</span><svg class="ic"><use href="#i-vegan"/></svg><svg class="ic"><use href="#i-gf"/></svg></div><p class="item-desc">Spinach, kale, cucumber, apple, and oranges.</p></div>
    <div class="item"><div class="item-name">Orange Turmeric Juice <span class="price">| 12.34</span><svg class="ic"><use href="#i-vegan"/></svg><svg class="ic"><use href="#i-gf"/></svg></div><p class="item-desc">Turmeric, ginger, lemon, carrot, and orange topped with cracked black pepper.</p></div>
    <div class="item"><div class="item-name">Fireshot <span class="price">| 12.34</span><svg class="ic"><use href="#i-vegan"/></svg><svg class="ic"><use href="#i-gf"/></svg></div><p class="item-desc">Ginger and lemon shot topped with cayenne.</p></div>
    <div class="item"><div class="item-name">Lemonade <span class="price">| 12.34</span></div><p class="item-desc">House Made Lemonade. Choice of unsweetened or agave sweetened in Regular, Raspberry, and Lavender flavors.</p></div>
    <div class="item"><div class="item-name">Tea <span class="price">| 12.34</span></div><p class="item-desc">Hot or iced</p></div>
  </div>

  <div class="photo" role="img" aria-label="Raspberry lemonade in a glass" style="left:196px;top:331px;width:75px;height:115px;background:linear-gradient(170deg,#f7a1a8,#ef5b6a 55%,#f6c4c8)"></div>
  <div class="block bg-white right" style="left:271px;top:331px;width:120px;height:115px;padding:6px 8px 0 4px">
    <h2 class="section-title" style="text-transform:none;font-size:10px">Bottled Drinks</h2>
    <div class="item"><div class="item-name" style="color:var(--ink)">Tallow Creek kombucha <span class="price">| 12.34</span></div><p class="item-desc" style="color:var(--orange)">(Fizzline Trilogy, Fizzline Gingerberry, Fizzline Mango)</p></div>
    <div class="item"><div class="item-name" style="color:var(--ink)">Brightwell <span class="price">| 12.34</span></div><p class="item-desc" style="color:var(--orange)">(Orange Mango, Lemon, Grapefruit)</p></div>
    <div class="item"><div class="item-name" style="color:var(--ink)">Palmera Original <span class="price">| 12.34</span></div></div>
    <div class="item"><div class="item-name" style="color:var(--ink)">Sparkling Water (Clearpeak) <span class="price">| 12.34</span></div></div>
    <div class="item"><div class="item-name" style="color:var(--ink)">Still Water (Clearpeak) <span class="price">| 12.34</span></div></div>
  </div>

  <div class="brand bg-white" style="left:391px;top:0;width:194px;height:131px">
    <span class="brand-dot"></span><span class="brand-name">Grubb Larder</span>
  </div>
  <div class="photo" role="img" aria-label="Salad with avocado, watermelon radish and citrus" style="left:391px;top:131px;width:194px;height:200px;background:radial-gradient(circle at 55% 55%,#c7d49a,#7c9a4a 45%,#c8c2b8 80%)"></div>
  <div class="closing bg-green" style="left:391px;top:331px;width:194px;height:115px;padding:12px 10px 0">
    <p class="closing-note">Our food is made with love:<br>love for humanity, love for flavor,<br>love for wellness,<br>and love for our customers<br>who love us back!</p>
    <p class="closing-contact">(818) 555-0142<br>Info@GrubbLarder.example<br>2417 W 83rd St, Los Angeles, CA 90247<br>www.GrubbLarder.example</p>
  </div>
</section>

<!-- Inside of the trifold -->
<section class="sheet sheet--inside">
  <div class="block bg-white" style="left:0;top:0;width:193px;height:243px">
    <h2 class="section-title">Breakfast</h2>
    <div class="item"><div class="item-name">Pastries <span class="price">| 12.34</span><svg class="ic"><use href="#i-veg"/></svg></div><p class="item-desc">Croissant (regular, almond, chocolate)<br><br>Blueberry Muffin<br><br>Superseed Cookie</p></div>
    <div class="item"><div class="item-name">Parfait <span class="price">| 12.34</span><svg class="ic"><use href="#i-veg"/></svg></div><p class="item-desc">Fresh strawberries and blueberries on yogurt and muesli and topped with honey drizzle.</p></div>
    <div class="item"><div class="item-name">Avocado Super Toast <span class="price">| 12.34</span><svg class="ic"><use href="#i-vegan"/></svg></div><p class="item-desc">Avocado Mash, Tomato, Basil, Ground Flax, Hemp Seed, Chickpeas, and Moringa Powder on Whole Wheat Bread.</p></div>
    <div class="item"><div class="item-name">Brunch Burger <span class="price">| 12.34</span></div><p class="item-desc">House seasoned beef burger topped with an over medium egg, red leaf lettuce, tomato, housemade pickles and Larder Sauce on a bun.</p></div>
    <div class="item"><div class="item-name">Breakfast Sammy <span class="price">| 12.34</span><svg class="ic"><use href="#i-vegan"/></svg><span class="note">Vegan Option</span></div><p class="item-desc">Your choice of over medium egg or tofu steak with guacamole, tomato, and Larder sauce on an English muffin.</p></div>
    <div class="item"><div class="item-name">AM Burrito <span class="price">| 12.34</span><svg class="ic"><use href="#i-veg"/></svg></div><p class="item-desc">Scrambled eggs, onion, red bell pepper, black beans, housemade salsa, yogurt, and pepper jack cheese in a tortilla.</p></div>
  </div>
  <div class="legend bg-cream" style="left:121px;top:0;width:72px;height:60px">
    <div class="legend-row"><svg class="ic"><use href="#i-vegan"/></svg>Vegan</div>
    <div class="legend-row"><svg class="ic"><use href="#i-veg"/></svg>Vegetarian</div>
    <div class="legend-row"><svg class="ic"><use href="#i-gf"/></svg>Gluten Free</div>
    <div class="legend-row"><svg class="ic"><use href="#i-nut"/></svg>Contains Nuts</div>
  </div>

  <div class="photo" role="img" aria-label="Purple berry smoothie in a glass" style="left:0;top:243px;width:63px;height:135px;background:linear-gradient(170deg,#b690c9,#8b5fa8 60%,#caa9d6)"></div>
  <div class="block bg-cream" style="left:63px;top:243px;width:130px;height:135px">
    <h2 class="section-title">Smoothies</h2>
    <div class="item"><div class="item-name">Green Machine Smoothie <span class="price">| 12.34</span><svg class="ic"><use href="#i-vegan"/></svg><svg class="ic"><use href="#i-gf"/></svg><svg class="ic"><use href="#i-nut"/></svg></div><p class="item-desc">Romaine, spinach, banana, mango, pineapple, flaxmilk, spirulina, almond butter.</p></div>
    <div class="item"><div class="item-name">Acai Smoothie <span class="price">| 12.34</span><svg class="ic"><use href="#i-vegan"/></svg><svg class="ic"><use href="#i-gf"/></svg><svg class="ic"><use href="#i-nut"/></svg></div><p class="item-desc">Acai, blueberries, banana, pineapple, Macqui berry, flaxmilk, almond butter.</p></div>
    <div class="item"><div class="item-name">Mango Smoothie <span class="price">| 12.34</span><svg class="ic"><use href="#i-vegan"/></svg><svg class="ic"><use href="#i-gf"/></svg></div><p class="item-desc">Mango, flaxmilk, banana, hemp seeds.</p></div>
  </div>

  <div class="block bg-green" style="left:193px;top:0;width:193px;height:243px">
    <h2 class="section-title">Bowls</h2>
    <div class="item"><div class="item-name">Southwest Bowl <span class="price">| 12.34</span><svg class="ic"><use href="#i-gf"/></svg><svg class="ic"><use href="#i-nut"/></svg></div><p class="item-desc">Your choice of protein with corn, black beans, red onions, almonds and avocado over quinoa with lime hot sauce.</p></div>
    <div class="item"><div class="item-name">Chimi Bowl <span class="price">| 12.34</span><svg class="ic"><use href="#i-gf"/></svg></div><p class="item-desc">Your choice of protein with red bell pepper, mushrooms, zucchini, squash, onion, cherry tomatoes and fresh herb chimichurri on wild and brown rice.</p></div>
    <div class="item"><div class="item-name">Soba Noodle Bowl <span class="price">| 12.34</span></div><p class="item-desc">Your choice of protein with spinach, snow peas, roasted carrots, red bell pepper, cilantro, sesame seeds and ginger lime sauce over soba noodles.</p></div>
    <div class="item"><div class="item-name">Hollywood Bowl <span class="price">| 12.34</span><svg class="ic"><use href="#i-gf"/></svg></div><p class="item-desc">Your choice of protein with broccoli, roasted corn, cherry tomatoes, basil, pepitas, flax seeds and lemon juice on wild and brown rice.</p></div>
    <div class="item"><div class="item-name">Larder Bowl <span class="price">| 12.34</span><svg class="ic"><use href="#i-gf"/></svg></div><p class="item-desc">Your choice of protein with roasted chickpeas and cauliflower, zesty fennel salad and citrus yogurt.</p></div>
    <div class="item"><div class="item-name">Buddha Bowl <span class="price">| 12.34</span></div><p class="item-desc">Your choice of protein with corn, red kale, sweet potatoes, red cabbage, parsley, oregano, hummus, and farro.</p></div>
    <div class="item"><div class="item-name">Chili Rice Bowl <span class="price">| 12.34</span><svg class="ic"><use href="#i-gf"/></svg></div><p class="item-desc">Chicken, onions, bell peppers, jalapeños, black &amp; kidney beans, and tomato over brown rice.</p></div>
  </div>

  <div class="block bg-orange" style="left:193px;top:243px;width:129px;height:135px">
    <h2 class="section-title">Soups</h2>
    <div class="item"><div class="item-name">Chicken Noodle <span class="price">| 12.34</span><svg class="ic"><use href="#i-gf"/></svg></div><p class="item-desc">Chicken, egg noodles, root vegetables, oregano &amp; peppercorns.</p></div>
    <div class="item"><div class="item-name">Larder Chili <span class="price">| 12.34</span><svg class="ic"><use href="#i-gf"/></svg></div><p class="item-desc">Chicken, onions, bell peppers, jalapeños, black &amp; kidney beans, and tomato.</p></div>
    <div class="item"><div class="item-name">Seasonal Rotating <span class="price">| 12.34</span><svg class="ic"><use href="#i-vegan"/></svg><svg class="ic"><use href="#i-gf"/></svg></div><p class="item-desc">(Butternut Squash Soup V+, GF) Butternut squash blended with warm spices, and coconut milk.</p></div>
  </div>
  <div class="photo" role="img" aria-label="Bowl of butternut squash soup with herbs" style="left:322px;top:243px;width:64px;height:135px;background:radial-gradient(circle at 50% 50%,#c98a2e,#b57a2a 45%,#e2e0dc 75%)"></div>

  <div class="block bg-white" style="left:386px;top:0;width:199px;height:217px">
    <h2 class="section-title">Salads</h2>
    <div class="item"><div class="item-name">Avocado, Golden Beet &amp; Cranberry Salad <span class="price">| 12.34</span><svg class="ic"><use href="#i-veg"/></svg><svg class="ic"><use href="#i-gf"/></svg></div><p class="item-desc">Gold beets, avocado, dried cranberries, watermelon radish, red kale, romaine, mixed greens, and pepitas served with Golden Buddha dressing.</p></div>
    <div class="item"><div class="item-name">Burrata Salad <span class="price">| 12.34</span><svg class="ic"><use href="#i-veg"/></svg><svg class="ic"><use href="#i-gf"/></svg></div><p class="item-desc">Tomato, melon, shredded basil, balsamic glaze, fresh cracked pepper, and olive oil with burrata.</p></div>
    <div class="item"><div class="item-name">Mediterranean Salad <span class="price">| 12.34</span><svg class="ic"><use href="#i-veg"/></svg><svg class="ic"><use href="#i-gf"/></svg></div><p class="item-desc">Cucumbers, Kalamata olives, cherry tomatoes, parsley, tricolor quinoa, hard-boiled egg, and hummus on mixed greens, romaine, and red cabbage with lemon-olive oil dressing.</p></div>
    <div class="item"><div class="item-name">Vegan Chef Salad <span class="price">| 12.34</span><svg class="ic"><use href="#i-vegan"/></svg><svg class="ic"><use href="#i-gf"/></svg><svg class="ic"><use href="#i-nut"/></svg></div><p class="item-desc">Roasted potatoes and carrots, chickpeas, avocado, microgreens and walnuts on mixed greens, romaine, and red kale with vegan ranch.</p></div>
    <div class="item"><div class="item-name">Rancher's Salad <span class="price">| 12.34</span><svg class="ic"><use href="#i-veg"/></svg><svg class="ic"><use href="#i-gf"/></svg></div><p class="item-desc">Tomato, red onion, hard boiled egg, avocado, feta cheese, microgreens, and grilled chicken on romaine with Ranch dressing.</p></div>
  </div>

  <div class="block bg-cream" style="left:386px;top:217px;width:136px;height:161px">
    <h2 class="section-title">Wraps</h2>
    <div class="item"><div class="item-name">Rancher's Wrap <span class="price">| 12.34</span></div><p class="item-desc">Tomato, red onion, hard boiled egg, avocado, feta cheese, microgreens, romaine, grilled chicken and Ranch dressing in a grilled wrap.</p></div>
    <div class="item"><div class="item-name">Vegan Tuna Wrap <span class="price">| 12.34</span><svg class="ic"><use href="#i-vegan"/></svg></div><p class="item-desc">Vegan tuna, romaine, avocado, celery, shallot, and oregano with Verdant Sauce in a whole grain wrap.</p></div>
    <div class="item"><div class="item-name">Vegetarian Wrap <span class="price">| 12.34</span><svg class="ic"><use href="#i-veg"/></svg></div><p class="item-desc">Roasted chickpeas, romaine, avocado, red bell pepper, shaved carrots, cucumber, spinach, basil, black beans and feta with lemon-hummus in a sprouted 7-grain wrap.</p></div>
  </div>
  <div class="photo" role="img" aria-label="Halved wraps filled with greens and vegetables" style="left:522px;top:217px;width:63px;height:161px;background:linear-gradient(165deg,#d9c7a0,#a7b860 45%,#c9684a 75%,#e4d6b4)"></div>

  <div class="photo" role="img" aria-label="Avocado toast with tomatoes" style="left:0;top:378px;width:65px;height:68px;background:linear-gradient(150deg,#8fae4a,#c7463a 55%,#a98a55)"></div>
  <div class="photo" role="img" aria-label="Mango smoothie" style="left:65px;top:378px;width:65px;height:68px;background:linear-gradient(160deg,#fbd35a,#f2b21f 60%,#f6e1a0)"></div>
  <div class="photo" role="img" aria-label="Burger with greens on a bun" style="left:130px;top:378px;width:65px;height:68px;background:linear-gradient(180deg,#c0763a,#7a4a2a 45%,#6e9a3c 70%,#c0864a)"></div>
  <div class="photo" role="img" aria-label="Strawberries, blueberries and granola" style="left:195px;top:378px;width:65px;height:68px;background:linear-gradient(140deg,#3e4a8a,#e0403a 50%,#e8d9c0)"></div>
  <div class="photo" role="img" aria-label="Green smoothie" style="left:260px;top:378px;width:65px;height:68px;background:linear-gradient(160deg,#7fae2c,#5e8f1c 60%,#a9c95c)"></div>
  <div class="photo" role="img" aria-label="Sandwich on a plate" style="left:325px;top:378px;width:65px;height:68px;background:linear-gradient(170deg,#d8d6d0,#b88a4a 45%,#7a9a4a 70%,#d8d6d0)"></div>
  <div class="photo" role="img" aria-label="Broccoli and tomato bowl" style="left:390px;top:378px;width:65px;height:68px;background:linear-gradient(150deg,#4f7d2a,#c9463a 50%,#6a9a34)"></div>
  <div class="photo" role="img" aria-label="Grain salad with vegetables" style="left:455px;top:378px;width:65px;height:68px;background:linear-gradient(150deg,#c9c3a8,#9cbf5a 50%,#e0d8c0)"></div>
  <div class="photo" role="img" aria-label="Salmon with green beans and carrots" style="left:520px;top:378px;width:65px;height:68px;background:linear-gradient(150deg,#e08a5a,#5a8a3a 50%,#e0762a)"></div>
</section>
</body>
</html>
```